Buchcover-Design für Fachbuch
Tolle Entwürfe und ein sehr effiziente Zusammenarbeit. Können wir nur weiterempfehlen.
Zielgruppe
Unternehmensberatung im Thema Arbeitszeit. Wir haben ein Fachbuch zum Thema Arbeitszeit und Personaleinsatzplanung für Geschäftsführer, HR Mitarbeiter, Führungskräfte, Studenten und alle geschrieben, die sich o.g. Themen näher informieren möchten
Aufgabenstellung
Folgende Textelemente sollen zu sehen sein:
Autorennamen: Dr. Reinhold Kattner, Lothar Brenning
Titel: PLAN STARK Betrieb - Dienstzeiten und Schichtorganisation fair, rentabel und marktnah einrichten
Außerdem: Unter Mitwirkung von Prof. Anton K. Ruhland
Und: mit vielen Praxisbeispielen (ggf. als eine Art Plakette)
Auf der Rückseite soll ein Klappentext und 2 Zitate zu sehen sein:
Klappentext:
Die Welt verändert sich dramatisch. Digitalisierung, Fachkräftemangel, Wertewandel und nicht zuletzt Ausnahmezustände wie die Coronakrise stellen Unternehmen vor große Herausforderungen. Wie können Unternehmen flexibel und gleichzeitig wirtschaftlich, kunden- und mitarbeiterorientiert agieren?
Reinhold Kattner und Lothar Brenning sehen eine innovative Arbeitszeitgestaltung als entscheidenden Hebel an, um Unternehmen aller Branchen in schnelllebigen Märkten flexibel aufzustellen. Die Autoren beleuchten mit vielen Beispielen aus ihrer Beratungspraxis, warum Arbeitszeitsysteme dringend modernisiert werden müssen und welche Möglichkeiten Sie bereits heute haben, Arbeitszeit innovativ zu gestalten.
Sie erfahren alles Wissenswerte über klassische Modelle, wie z.B. Schichtplan, Gleitzeit, Vertrauensarbeitszeit, Zeitkontensystem und Teilzeit, über Workforce Management (Workforce Analytics, Personalbedarfsermittlung und Forecast, Personaleinsatzplanung, Zeiterfassung) bis hin zu Lebensarbeitszeit, Gruppenarbeit, Selbstorganisation, Homeoffice und New Work. Dabei lernen Sie nicht nur die Einzelkomponenten kennen, sondern erfahren auch, wie man diese geschickt zu einer für Mitarbeiter und Unternehmen gleichermaßen vorteilhaften Arbeitszeitsystematik kombiniert. Neben diesem strategischen Wissen vermitteln Ihnen die Autoren hilfreiche Methoden zur konkreten operativen Umsetzung dieser Themen.
Zitat 1:
„Durch die Weitergabe ihrer umfassenden Erfahrungen aus der Beratung ist es den Autoren in hervorragender Weise gelu..

```html
<!DOCTYPE html>
<html lang="de">
<head>
<meta charset="utf-8">
<title>PLAN STARK Betrieb – Buchcover</title>
<link href="https://fonts.googleapis.com/css2?family=Bebas+Neue&family=Heebo:wght@300;400&display=swap" rel="stylesheet">
<style>
  :root {
    --navy: #003873;
    --green: #9bc43c;
    --lavender: #8f9dc4;
    --orange: #f0a800;
    --white: #ffffff;
    --page: #ffffff;
  }
  * { margin: 0; padding: 0; box-sizing: border-box; }
  html, body { width: 848px; height: 1200px; overflow: hidden; background: var(--page); }
  .canvas { position: relative; width: 848px; height: 1200px; font-family: "Heebo", sans-serif; }
  .cover { position: absolute; left: 81px; top: 190px; width: 686px; height: 889px; background: var(--white); border: 1px solid #d8d8d8; }
  .block { position: absolute; }

  .photo-doctors { left: 0; top: 0; width: 228px; height: 203px; background: linear-gradient(135deg, #eef2f6, #c9d4df 60%, #a9b9c9); }
  .author-box { left: 228px; top: 0; width: 229px; height: 183px; background: var(--navy); color: var(--white);
    display: flex; flex-direction: column; justify-content: center; align-items: center; font-size: 22px; line-height: 32px; padding-bottom: 8px; }
  .strip-top { left: 228px; top: 183px; width: 229px; height: 20px; background: var(--lavender); }
  .photo-cashier { left: 457px; top: 0; width: 229px; height: 203px; background: linear-gradient(135deg, #8a8f97, #c9b9a2 50%, #8aa2c0); }

  .title-area { left: 0; top: 203px; width: 686px; height: 281px; }
  .bar-green { left: 0; top: 0; width: 20px; height: 201px; background: var(--green); }
  .bar-navy { left: 0; top: 201px; width: 20px; height: 80px; background: var(--navy); }
  .title { position: absolute; left: 42px; top: 14px; font-family: "Bebas Neue", sans-serif; line-height: 1; }
  .title-small { color: var(--green); font-size: 80px; letter-spacing: 1px; }
  .title-big { display: flex; gap: 14px; font-size: 148px; margin-top: -8px; letter-spacing: 1px; }
  .title-big .green { color: var(--green); }
  .title-big .navy { color: var(--navy); }

  .strip-bottom { left: 0; top: 484px; width: 457px; height: 20px; background: var(--lavender); }
  .subtitle-box { left: 0; top: 504px; width: 457px; height: 183px; background: var(--navy); color: var(--white);
    font-weight: 300; font-size: 30px; line-height: 36px; padding: 22px 0 0 30px; }
  .photo-office { left: 457px; top: 484px; width: 229px; height: 203px; background: linear-gradient(135deg, #f3f4f5, #dfe2e6 55%, #c7ccd2); }
  .photo-bakery { left: 0; top: 687px; width: 457px; height: 202px; background: linear-gradient(135deg, #d9c3a1, #ece7df 50%, #a3a7ab); }
  .contrib-box { left: 457px; top: 687px; width: 229px; height: 202px; background: var(--green); color: var(--white); text-align: center; padding-top: 83px; }
  .contrib-label { font-size: 15px; line-height: 20px; }
  .contrib-name { font-size: 21px; line-height: 30px; margin-top: 2px; }

  .badge { position: absolute; left: 381px; top: 598px; width: 170px; height: 170px; }
</style>
</head>
<body>
<div class="canvas">
  <div class="cover">
    <div class="block photo-doctors" role="img" aria-label="Foto: Ärzteteam bespricht sich am Laptop"></div>
    <div class="block author-box">
      <span>Dr. Reinhold Kattner</span>
      <span>Lothar Brenning</span>
    </div>
    <div class="block strip-top"></div>
    <div class="block photo-cashier" role="img" aria-label="Foto: Kassierer an der Supermarktkasse"></div>

    <div class="block title-area">
      <div class="block bar-green"></div>
      <div class="block bar-navy"></div>
      <h1 class="title">
        <div class="title-small">PLAN</div>
        <div class="title-big"><span class="green">STARK</span><span class="navy" style="font-size:118px;align-self:flex-end;">BETRIEB</span></div>
      </h1>
    </div>

    <div class="block strip-bottom"></div>
    <div class="block subtitle-box">Dienstzeiten und Schicht-<br>organisation fair, rentabel<br>und marktnah einrichten</div>
    <div class="block photo-office" role="img" aria-label="Foto: Mitarbeiterin am Laptop im Büro"></div>
    <div class="block photo-bakery" role="img" aria-label="Foto: Bäckerinnen in der Backstube"></div>
    <div class="block contrib-box">
      <div class="contrib-label">Unter Mitwirkung von</div>
      <div class="contrib-name">Prof. Anton K. Ruhland</div>
    </div>

    <svg class="badge" viewBox="0 0 170 170" aria-label="mit vielen Praxisbeispielen">
      <circle cx="85" cy="85" r="82" fill="var(--orange)" stroke="var(--white)" stroke-width="4"/>
      <g transform="rotate(-6 85 85)" font-family="Heebo, sans-serif" font-size="26" fill="var(--white)" text-anchor="middle">
        <text x="85" y="66">mit vielen</text>
        <text x="85" y="95">Praxis-</text>
        <text x="85" y="124">beispielen</text>
      </g>
    </svg>
  </div>
</div>
</body>
</html>
```